Zub Programming Video Tutorial Blog

Please be aware I am flexible with budget, I will increase it for great design thanks

A blog (wordpress) design required for video blogging teaching Zub Programming (creating quorbit apps). There are 4 pages required to be designed, the landing page where user submit their name and email (also shows an intro video), the main video blogging page (with beautiful video placeholder), a normal text blog page with big image at the top of each post and finally the portfolio page. The portfolio is where the tutor showcase all his previous developed apps and other projects to show his expertise.

The colour combination preferred are a mixture of blue and orange but we are open to other beautiful color combinations. Minimalistic design with lots of white and clare objectives for each page. The design should reflect the purpose of the website, someone who cannot read english landing on the page should immediately realise the page is made for learning to design quorbit apps.

I like curves and round corners, especially comment and portfolio pages with curves etc thanks

The blog domain will be brelvanta.example
Updates

Target Market(s)

new programmer on the quorbit platform

Industry/Entity Type

Learning

Requirements
Must have
• quorbit image in the design
landing page has a video intro and Quorbit/vexa image
Nice to have
• curves. round corners and circular shapes

```html
<!DOCTYPE html>
<html lang="en">
<head>
<meta charset="utf-8">
<title>Brelvanta – Our Blog</title>
<link href="https://fonts.googleapis.com/css2?family=Fredoka:wght@600&family=Open+Sans:ital,wght@0,400;0,600;0,700;1,400&display=swap" rel="stylesheet">
<style>
:root{
  --blue:#1a8ae0;
  --blue-dark:#1479c9;
  --blue-text:#1f86d8;
  --orange:#ff6a00;
  --ink:#1b1b1b;
  --body:#555;
  --muted:#8a8a8a;
  --rule:#c9cdd1;
  --panel-dark:#4a4a4a;
  --page:#eceff2;
  --white:#fff;
}
*{box-sizing:border-box;margin:0;padding:0}
html,body{width:786px;height:1200px;overflow:hidden}
body{position:relative;font-family:"Open Sans",Arial,sans-serif;color:var(--body);
  background:linear-gradient(180deg,#dfe7ee 0,#eef1f4 300px,#f1f2f3 797px)}
.abs{position:absolute}

/* header */
.site-header{position:absolute;left:0;top:0;width:786px;height:50px;background:var(--blue)}
.user-bar{position:absolute;left:561px;top:0;width:111px;height:13px;background:#3f9ee6;
  font-size:7px;color:#fff;line-height:13px;padding-left:6px}
.user-bar .avatar{display:inline-block;width:7px;height:7px;background:#e7b08a;border-radius:1px;vertical-align:-1px;margin-right:3px}
.brand{position:absolute;left:113px;top:11px;font-family:"Fredoka",sans-serif;font-weight:600;font-size:24px;color:#fff;line-height:28px}
.main-nav a{position:absolute;top:21px;font-size:9px;font-weight:700;color:#fff;text-decoration:none;letter-spacing:.2px}
.main-nav a.active{border-bottom:1.5px solid #fff;padding-bottom:3px}

/* headings */
.section-title{position:absolute;font-family:"Fredoka",sans-serif;font-weight:600;color:var(--blue-text);font-size:24px;line-height:28px}
.title-rule{position:absolute;height:1px;background:#4a88c4}
.post-title{position:absolute;left:113px;top:126px;font-family:"Fredoka",sans-serif;font-weight:600;font-size:18px;color:var(--ink)}
.post-title::before{content:"↓";font-family:"Open Sans",sans-serif;font-weight:700;font-size:15px;margin-right:4px}
.hr{position:absolute;height:1px;background:var(--rule)}
.meta{position:absolute;left:113px;top:166px;font-size:10px;color:#666;display:flex;gap:16px;align-items:center}
.meta span{display:flex;align-items:center;gap:5px}
.meta svg{fill:#b5b5b5}

/* feature image */
.post-figure{position:absolute;left:113px;top:203px;width:386px;height:226px;background:#fff;border:1px solid #dcdcdc;border-radius:3px;box-shadow:0 1px 3px rgba(0,0,0,.12);padding:5px}
.post-figure .photo{width:100%;height:100%;background:linear-gradient(160deg,#c6ccd0 0%,#7d8790 40%,#3b3f44 75%,#d7d5cf 100%)}

.post-body{position:absolute;left:116px;top:455px;width:382px;font-size:9.2px;line-height:13.2px;color:#555}
.post-body p{margin-bottom:12.8px}

/* share counts */
.share-row{position:absolute;left:113px;top:754px;display:flex;gap:10px;font-size:6px;color:#444}
.share{display:flex;align-items:center;gap:2px}
.share b{display:inline-block;border:1px solid #c9c9c9;background:#f5f5f5;padding:1px 4px;border-radius:2px;font-weight:600}
.share i{font-style:normal;border:1px solid #d0d0d0;background:#fff;padding:1px 3px;border-radius:2px}

/* comments area */
.comments-band{position:absolute;left:0;top:797px;width:786px;height:343px;background:var(--white);border-top:1px solid #dadada}
.comment{position:absolute;left:113px;width:387px}
.comment .who{font-size:9px;font-weight:600;color:var(--blue-text);display:flex;align-items:center;gap:4px}
.comment .when{position:absolute;right:0;top:1px;font-size:7.5px;font-style:italic;color:#999}
.comment p{margin-top:7px;font-size:8.6px;line-height:10px;font-style:italic;color:#555}

.field{position:absolute;border:1px solid #b8b8b8;border-radius:4px;background:#fff;font-size:9.5px;color:#888;padding:5px 7px}
.btn-post{position:absolute;left:384px;top:1097px;width:115px;height:22px;background:var(--orange);border-radius:2px;color:#fff;font-family:"Fredoka",sans-serif;font-weight:600;font-size:11px;line-height:22px;text-align:center}

/* sidebar */
.sidebar{position:absolute;left:517px;top:79px;width:155px;height:527px;background:#fff;box-shadow:0 0 2px rgba(0,0,0,.1)}
.sidebar-head{position:absolute;left:0;width:155px;background:var(--panel-dark);color:#fff}
.sidebar-head h3{font-family:"Open Sans",sans-serif;font-weight:700;font-size:11.5px}
.recent-item{position:absolute;left:0;width:155px;height:64px;border-bottom:1px solid #ececec}
.recent-item .thumb{position:absolute;left:14px;top:17px;width:41px;height:41px}
.recent-item h4{position:absolute;left:60px;top:18px;font-size:8.8px;font-weight:700;color:var(--blue-text)}
.recent-item p{position:absolute;left:60px;top:29px;width:82px;font-size:8px;line-height:9.5px;color:#555}
.map{position:absolute;left:15px;top:331px;width:127px;height:84px;border:1px solid #ddd;border-radius:3px;padding:3px;background:#fff}
.map div{width:100%;height:100%;background:linear-gradient(135deg,#e8e4d8 0%,#ddd9cc 55%,#7fb4e2 80%,#5ea3de 100%)}
.contact-card{position:absolute;left:34px;top:428px;font-size:7.6px;line-height:9.6px;color:#222}
.contact-card b{display:block;font-size:8.8px;color:var(--blue-text);margin-bottom:1px}
.phone{position:absolute;left:34px;top:486px;font-size:13px;color:var(--blue-text)}

/* footer */
.site-footer{position:absolute;left:0;top:1140px;width:786px;height:60px;background:var(--blue);color:#fff;font-size:7.5px}
.site-footer .links{position:absolute;left:113px;top:22px}
.site-footer .legal{position:absolute;left:113px;top:33px}
.site-footer .legal a{color:#69d0ff;text-decoration:none}
.social-dot{position:absolute;top:16px;width:25px;height:25px;border-radius:50%;background:#4da5e8}
</style>
</head>
<body>

<header class="site-header">
  <div class="user-bar"><span class="avatar"></span>Hi, Mira Solvang &nbsp;|&nbsp; Logout</div>
  <div class="brand">Brelvanta</div>
  <nav class="main-nav">
    <a style="left:443px">HOME</a>
    <a class="active" style="left:488px">ABOUT DEVELOPER</a>
    <a style="left:589px">BLOG</a>
    <a style="left:629px">CONTACT</a>
  </nav>
</header>

<main>
  <h1 class="section-title" style="left:113px;top:78px">Our Blog</h1>
  <div class="title-rule" style="left:218px;top:103px;width:278px"></div>

  <h2 class="post-title">Lorem ipsum dolor amet consectetur</h2>
  <div class="hr" style="left:113px;top:160px;width:386px"></div>

  <div class="meta">
    <span><svg width="10" height="10" viewBox="0 0 10 10"><rect x="0" y="1" width="10" height="9" rx="1"/><rect x="1.5" y="3.5" width="7" height="5" fill="#fff"/></svg>10, July 2013</span>
    <span><svg width="10" height="10" viewBox="0 0 10 10"><circle cx="5" cy="5" r="5"/></svg>By Orin Vale</span>
    <span><svg width="11" height="10" viewBox="0 0 11 10"><path d="M0 0h11v7H4L1 10V7H0z"/></svg>Comment 192</span>
  </div>

  <figure class="post-figure">
    <div class="photo" role="img" aria-label="Photo of a busy open-plan office with developers working at computer desks"></div>
  </figure>

  <article class="post-body">
    <p>Lorem ipsum dolor sit amet, consectetur adipisicing elit, sed do eiusmod tempor incididunt ut labore et dolore magna aliqua. Ut enim ad minim veniam, quis nostrud exercitation ullamco laboris nisi ut aliquip ex ea commodo consequat.</p>
    <p>Duis aute irure dolor in reprehenderit in voluptate velit esse cillum dolore eu fugiat nulla pariatur. Excepteur sint occaecat cupidatat non proident, sunt in culpa qui officia deserunt mollit anim id est laborum.</p>
    <p>Lorem ipsum dolor sit amet, consectetur adipisicing elit, sed do eiusmod tempor incididunt ut labore et dolore magna aliqua. Ut enim ad minim veniam, quis nostrud exercitation ullamco laboris nisi ut aliquip ex ea commodo consequat.</p>
    <p>Duis aute irure dolor in reprehenderit in voluptate velit esse cillum dolore eu fugiat nulla pariatur. Excepteur sint occaecat cupidatat non proident, sunt in culpa qui officia deserunt mollit anim id est laborum.</p>
    <p>Lorem ipsum dolor sit amet, consectetur adipisicing elit, sed do eiusmod tempor incididunt ut labore et dolore magna aliqua. Ut enim ad minim veniam, quis nostrud exercitation ullamco laboris nisi ut aliquip ex ea commodo consequat. Duis aute irure dolor in reprehenderit in voluptate velit esse cillum dolore eu fugiat nulla pariatur.</p>
  </article>

  <div class="hr" style="left:113px;top:747px;width:386px"></div>
  <div class="share-row">
    <span class="share"><b>Post</b><i>466</i></span>
    <span class="share"><b>Share</b><i>299</i></span>
    <span class="share"><b>Like</b><i>490</i></span>
    <span class="share"><b>Plus</b><i>96</i></span>
  </div>

  <aside class="sidebar">
    <div class="sidebar-head" style="top:0;height:86px;padding:18px 16px">
      <h3>Recent Blog</h3>
      <p style="font-size:8.4px;line-height:10px;margin-top:8px">Lorem ipsum dolor sit amet, consectetur adipisicing elit sed do eiusmod</p>
    </div>
    <div class="recent-item" style="top:86px">
      <div class="thumb" role="img" aria-label="Blog post thumbnail" style="top:12px;background:linear-gradient(135deg,#8a2fb5,#5b1b80)"></div>
      <h4 style="top:13px">Blog Title</h4><p style="top:24px">Lorem ipsum dolor sit amet adipisicing dolor sit amet..</p>
    </div>
    <div class="recent-item" style="top:150px">
      <div class="thumb" role="img" aria-label="Blog post thumbnail" style="top:12px;background:linear-gradient(135deg,#d9d9d9,#bdbdbd)"></div>
      <h4 style="top:13px">Blog Title</h4><p style="top:24px">Lorem ipsum dolor sit amet adipisicing dolor sit amet..</p>
    </div>
    <div class="recent-item" style="top:214px;border:0">
      <div class="thumb" role="img" aria-label="Blog post thumbnail" style="top:12px;background:linear-gradient(135deg,#b9c4cc,#4d5a66)"></div>
      <h4 style="top:13px">Blog Title</h4><p style="top:24px">Lorem ipsum dolor sit amet adipisicing dolor sit amet..</p>
    </div>
    <div class="sidebar-head" style="top:291px;height:27px;padding:7px 16px"><h3>Contact us</h3></div>
    <div class="map"><div role="img" aria-label="Street map showing the office location"></div></div>
    <svg class="abs" style="left:18px;top:430px" width="10" height="14" viewBox="0 0 10 14"><path d="M5 0a5 5 0 0 1 5 5c0 4-5 9-5 9S0 9 0 5a5 5 0 0 1 5-5z" fill="var(--blue-text)"/><circle cx="5" cy="5" r="2" fill="#fff"/></svg>
    <div class="contact-card"><b>Lena Marsh</b>Brelvanta<br>4120 Harbor Crest Rd,<br>Ste 210, Fairmont,<br>NC 28900-0412</div>
    <svg class="abs" style="left:18px;top:489px" width="12" height="12" viewBox="0 0 12 12"><path d="M2 0l3 3-1.5 2a7 7 0 0 0 3.5 3.5L9 7l3 3-2 2C5 12 0 7 0 2z" fill="var(--blue-text)"/></svg>
    <div class="phone">(555) 014-2290</div>
  </aside>
</main>

<section class="comments-band">
  <div class="comment" style="top:29px">
    <div class="who"><svg width="11" height="9" viewBox="0 0 11 9"><path d="M0 0h11v7H4L2 9V7H0z" fill="var(--blue-text)"/></svg>Tomas Reed - USA</div>
    <span class="when">Posted on 10, July 2013</span>
    <p>Lorem ipsum dolor sit amet, consectetur adipisicing elit, sed do eiusmod tempor incididunt ut labore et dolore magna aliqua. Ut enim ad minim venia.</p>
  </div>
  <div class="hr" style="left:113px;top:81px;width:387px;background:#e2e2e2"></div>
  <div class="comment" style="top:93px">
    <div class="who"><svg width="11" height="9" viewBox="0 0 11 9"><path d="M0 0h11v7H4L2 9V7H0z" fill="var(--blue-text)"/></svg>Tomas Reed - USA</div>
    <span class="when">Posted on 10, July 2013</span>
    <p>Lorem ipsum dolor sit amet, consectetur adipisicing elit, sed do eiusmod tempor incididunt ut labore et dolore magna aliqua. Ut enim ad minim venia.</p>
  </div>
</section>

<h2 class="section-title" style="left:113px;top:943px;font-size:19px">Post Coment</h2>
<div class="title-rule" style="left:223px;top:962px;width:276px"></div>
<div class="field" style="left:113px;top:989px;width:188px;height:23px">User Name</div>
<div class="field" style="left:313px;top:989px;width:187px;height:23px">Email ID</div>
<div class="field" style="left:113px;top:1020px;width:387px;height:61px">Commens</div>
<div class="btn-post">Post Comment →</div>

<footer class="site-footer">
  <div class="links">Home &nbsp;-&nbsp; About &nbsp;-&nbsp; Blog &nbsp;-&nbsp; Contact</div>
  <div class="legal">© 2013 &nbsp;-&nbsp; Terms and Conditions &nbsp;-&nbsp; Email : <a>info@brelvanta.example</a></div>
  <span class="social-dot" style="left:587px"></span>
  <span class="social-dot" style="left:617px"></span>
  <span class="social-dot" style="left:647px"></span>
</footer>

</body>
</html>
```